Vitaroot gym flyer

Use the text offered in the word document and add the appropriate images in the space provided. The images may need to be resized.Can the font be bold and silver with a black outline.Can the background be light blue.I have submitted a design request for some business cards. I'd like the cards and the flyer to match.

Industry/Entity Type

Gym

```html
<!DOCTYPE html>
<html lang="en">
<head>
<meta charset="utf-8">
<title>Vitaroot Gym Flyer</title>
<link href="https://fonts.googleapis.com/css2?family=Cinzel:wght@700;900&family=Signika:ital,wght@0,500;0,700;1,700&display=swap" rel="stylesheet">
<style>
  :root {
    --bg-light: #b4f4ec;
    --bg-mid: #86e3da;
    --bg-deep: #5ccfc6;
    --silver: #dcdcdc;
    --silver-hi: #f6f6f6;
    --outline: #1a1a1a;
    --name-red: #7a0f14;
    --sub-grey: #3c4a4c;
    --photo-a: #c9b7a6;
    --photo-b: #3a3236;
    --photo-c: #b98c72;
    --photo-d: #6b5c55;
  }
  * { margin: 0; padding: 0; box-sizing: border-box; }
  html, body { width: 1200px; height: 850px; overflow: hidden; }
  body { background: var(--bg-mid); }
  .flyer {
    position: relative;
    width: 1200px; height: 850px;
    overflow: hidden;
    background: linear-gradient(180deg, var(--bg-light) 0%, var(--bg-mid) 55%, var(--bg-deep) 100%);
    font-family: "Cinzel", serif;
  }
  .gym-backdrop {
    position: absolute; left: 0; right: 0; bottom: 0; height: 500px;
    background: linear-gradient(180deg, rgba(255,255,255,0) 0%, rgba(60,150,145,0.25) 60%, rgba(40,120,118,0.3) 100%);
  }
  .photo {
    position: absolute;
    box-shadow: 0 4px 14px rgba(0,0,0,0.35);
  }
  .photo--left {
    left: 127px; top: 53px; width: 330px; height: 365px;
    transform: rotate(-13deg);
    background: linear-gradient(90deg, var(--photo-a) 0%, var(--photo-a) 47%, #ffffff 47%, #ffffff 48.5%, var(--photo-b) 48.5%, var(--photo-b) 100%);
  }
  .photo--right {
    left: 716px; top: 72px; width: 388px; height: 331px;
    transform: rotate(14deg);
    background: linear-gradient(90deg, var(--photo-c) 0%, var(--photo-d) 47%, #ffffff 47%, #ffffff 48.5%, var(--photo-c) 48.5%, #9a8f86 100%);
  }
  .client {
    position: absolute;
    text-align: center;
    line-height: 1;
  }
  .client__name {
    font-family: "Cinzel", serif; font-weight: 900;
    font-size: 30px; color: var(--name-red);
    text-shadow: 0 0 6px rgba(255,255,255,0.9), 0 0 2px #fff;
  }
  .client__role, .client__age {
    font-family: "Signika", sans-serif; font-weight: 500;
    font-size: 25px; color: var(--sub-grey);
    text-shadow: 0 0 5px #fff, 0 0 2px #fff;
    margin-top: 2px;
  }
  .client--therapist { left: 546px; top: 42px; width: 300px; }
  .client--beautician { left: 400px; top: 305px; width: 300px; }
  .silver {
    color: var(--silver);
    -webkit-text-stroke: 1.2px var(--outline);
    text-shadow: 0 1px 0 var(--silver-hi), 1px 2px 2px rgba(0,0,0,0.45);
    font-family: "Cinzel", serif; font-weight: 900;
  }
  .line {
    position: absolute; left: 0; width: 1200px;
    text-align: center; white-space: nowrap; line-height: 1;
  }
  .headline { font-size: 29px; letter-spacing: 1px; }
  .headline--one { top: 462px; }
  .headline--two { top: 497px; }
  .coach { top: 566px; font-size: 25px; letter-spacing: 0.5px; }
  .offer { top: 598px; font-size: 26px; letter-spacing: 0.5px; }
  .contact { top: 630px; font-size: 38px; letter-spacing: 0.5px; }
  .divider {
    position: absolute; left: 14px; top: 682px; width: 1172px; height: 0;
    border-top: 4px dashed #111;
  }
  .stats-title {
    top: 700px;
    font-family: "Signika", sans-serif; font-style: italic; font-weight: 700;
    font-size: 31px; color: #555;
    -webkit-text-stroke: 1px var(--outline);
  }
  .stats-row {
    top: 749px;
    font-family: "Cinzel", serif; font-weight: 700;
    font-size: 19px; color: var(--name-red);
    letter-spacing: 0.4px;
  }
  .cta { top: 786px; font-size: 38px; color: #f2f2f2; letter-spacing: 0.5px; }
</style>
</head>
<body>
<main class="flyer">
  <div class="gym-backdrop" role="img" aria-label="Faded photo of treadmills in a gym"></div>

  <div class="photo photo--left" role="img" aria-label="Before and after photos of Sophie Marlow, first holding a newborn, then standing slim in a black outfit"></div>
  <div class="photo photo--right" role="img" aria-label="Before and after photos of Mark Delaney in shorts, labelled Then and Now"></div>

  <div class="client client--therapist">
    <div class="client__name">Mark Delaney</div>
    <div class="client__role">Sports Therapist</div>
    <div class="client__age">Age 35</div>
  </div>

  <div class="client client--beautician">
    <div class="client__name">Sophie Marlow</div>
    <div class="client__role">Beautician</div>
    <div class="client__age">Age 35</div>
  </div>

  <p class="line silver headline headline--one">Get your body looking exactly how you</p>
  <p class="line silver headline headline--two">want it to and more importantly... KEEP IT THAT WAY</p>

  <p class="line silver coach">Wellness &amp; Body Transformation Coach</p>
  <p class="line silver offer">Call Liam for a FREE and unique body evaluation tailored to YOU.</p>
  <p class="line silver contact">07700 900 482 Social: Liam Hartwell</p>

  <div class="divider"></div>

  <p class="line stats-title">Your Stats:</p>
  <p class="line stats-row">Weight:............... Body Fat %:.............. Metabolic Age: .............. Muscle Mass %:.............. Water Hydration: ...............</p>

  <p class="line silver cta">Don't like your stats? Call Liam 07700 900 482 Today.</p>
</main>
</body>
</html>
```